Cloud Backup Software Icons & image Design

-----Revised
This project requires and icon in 3 sizes and 4 images to be used in a software screen, please read the attached PDF document called "Software Icons" for instructions on image type, size and resolution.

We are calling the product "Talvero Netwise Cloud Backup & Recovery" this does not need to all be in one line.

Looking for clean professional design, I will post some splash screens that I like in the brief and this is my idead

IDEA:

Take a look at my website talveronetwise.com what if the splash screen was similar, green slender stripe up top white in the middle and a gray/black at the bottom.

My existing logo (attached in brief) was off to the left and to the right of the logo after a pipe " | Cloud Backup & Recovery"

Faded in the splash screen was a few shields of different sizes as well as faded in blue or outline in green the images of a server, database and a PC being backed up to a cloud.

The icon can incorporate my shield and a cloud. The splash screen is a starting point for the other images.

Industry/Entity Type

Information Technology

Requirements
Must have
• Splash screen: We do want an icon to the left like the existing as well as the company logo (attached) in the bottom right.
Should not have
• Stock Images

```html
<!DOCTYPE html>
<html lang="en">
<head>
<meta charset="utf-8">
<title>Talvero Netwise – Software Image Set</title>
<link rel="stylesheet" href="https://fonts.googleapis.com/css2?family=Montserrat:wght@500;600;700&family=Open+Sans:wght@400&display=swap">
<style>
  :root{
    --navy:#0d3b70;
    --green:#6cbf45;
    --green-deep:#55b94a;
    --lime:#a6cf58;
    --sky:#7fcdf0;
    --cream:#fdf9cc;
    --pale:#f3f7e4;
    --white:#ffffff;
    --label:#222222;
    --disc:#e6e8ea;
  }
  html,body{margin:0;padding:0;width:1045px;height:1200px;overflow:hidden;background:var(--white);}
  .sheet{position:relative;width:1230px;height:1412px;transform:scale(.85);transform-origin:0 0;font-family:"Montserrat",sans-serif;}
  .label{position:absolute;font-family:"Open Sans",sans-serif;font-weight:400;font-size:20px;color:var(--label);white-space:nowrap;margin:0;}
  .label.small{font-size:18px;}
  .art{position:absolute;overflow:hidden;}
  .art.open{overflow:visible;}
  .mark{position:absolute;border-radius:50%;}
  .wordmark{position:absolute;color:var(--navy);font-weight:700;letter-spacing:.08em;line-height:1;white-space:nowrap;margin:0;}
  .tagline{position:absolute;color:var(--navy);font-weight:500;letter-spacing:.06em;white-space:nowrap;margin:0;line-height:1;}
  .disc{position:absolute;border-radius:50%;background:radial-gradient(circle at 40% 40%,#fafafa,var(--disc) 70%,#cfd3d6);}

  /* splash */
  .splash{left:60px;top:100px;width:643px;height:421px;
    background:
      linear-gradient(180deg,rgba(255,255,255,0) 45%,var(--pale) 100%),
      linear-gradient(90deg,var(--sky) 0%,#9fd3b8 30%,var(--lime) 60%,var(--cream) 90%);}
  .splash .reserve{position:absolute;left:440px;top:4px;width:192px;height:118px;border:2px solid var(--lime);box-sizing:border-box;}
  .splash .brand{position:absolute;left:200px;top:170px;color:var(--white);font-size:26px;font-weight:600;letter-spacing:.12em;line-height:1;}
  .splash .title{position:absolute;left:197px;top:192px;margin:0;color:var(--navy);font-size:53px;font-weight:700;white-space:nowrap;}
  .loading{left:60px;top:521px;width:644px;height:35px;background:linear-gradient(90deg,#6cbf45,var(--green-deep) 50%,#d2e05c);}
  .loading span{position:absolute;left:25px;top:7px;color:var(--white);font-size:18px;font-weight:500;line-height:1.1;}

  /* top banner */
  .top-banner{left:61px;top:637px;width:608px;height:113px;
    background:linear-gradient(90deg,#86cbe3 0%,#9fd0a6 30%,var(--lime) 55%,var(--cream) 100%);}

  /* wizard left panel */
  .wizard-panel{left:783px;top:100px;width:263px;height:700px;
    background:linear-gradient(180deg,var(--cream) 0%,#eef5d6 30%,#b6d97a 45%,#a5d3b0 70%,var(--sky) 100%);}

  /* left panel */
  .left-panel{left:784px;top:872px;width:252px;height:481px;
    background:linear-gradient(180deg,#b8d97a 0%,#eef4d6 25%,#a7d4b5 60%,var(--sky) 100%);}
</style>
</head>
<body>
<main class="sheet">

  <h2 class="label" style="left:63px;top:64px;">Splash screen&nbsp; 436x310</h2>
  <section class="art splash" aria-label="Splash screen">
    <div class="mark" style="left:35px;top:20px;width:190px;height:190px;background:rgba(255,255,255,.9);"></div>
    <div class="reserve"></div>
    <span class="brand">TALVERO</span>
    <h1 class="title">Online Backup</h1>
    <div class="mark" style="left:470px;top:350px;width:34px;height:34px;background:var(--navy);"></div>
    <p class="wordmark" style="left:512px;top:357px;font-size:11px;">TALVERO NETWISE</p>
    <p class="tagline" style="left:512px;top:373px;font-size:6px;">Cloud Backup &amp; Recovery</p>
  </section>
  <div class="art loading"><span>Loading...</span></div>

  <h2 class="label" style="left:63px;top:600px;">Top banner&nbsp; 413x77</h2>
  <section class="art top-banner" aria-label="Top banner">
    <div class="mark" style="left:165px;top:12px;width:90px;height:90px;background:var(--navy);"></div>
    <p class="wordmark" style="left:287px;top:32px;font-size:27px;">TALVERO</p>
    <p class="wordmark" style="left:287px;top:60px;font-size:20px;">NETWISE</p>
    <p class="tagline" style="left:288px;top:84px;font-size:13px;">Cloud Backup &amp; Recovery</p>
  </section>

  <h2 class="label" style="left:64px;top:853px;">Wizard banner&nbsp; 141x72</h2>
  <section class="art open" style="left:60px;top:900px;width:260px;height:78px;" aria-label="Wizard banner">
    <div class="mark" style="left:2px;top:6px;width:64px;height:64px;background:var(--navy);"></div>
    <p class="wordmark" style="left:96px;top:24px;font-size:16px;">TALVERO</p>
    <p class="wordmark" style="left:96px;top:43px;font-size:12px;">NETWISE</p>
    <p class="tagline" style="left:96px;top:60px;font-size:9px;">Cloud Backup &amp; Recovery</p>
  </section>

  <h2 class="label small" style="left:74px;top:1084px;">16x16</h2>
  <div class="mark" style="left:81px;top:1122px;width:38px;height:38px;background:var(--navy);"></div>
  <h2 class="label small" style="left:214px;top:1069px;">32x32</h2>
  <div class="mark" style="left:205px;top:1103px;width:68px;height:68px;background:var(--navy);"></div>
  <h2 class="label small" style="left:375px;top:1052px;">48x48</h2>
  <div class="mark" style="left:350px;top:1090px;width:106px;height:106px;background:var(--navy);"></div>

  <h2 class="label" style="left:785px;top:69px;">Wizard left panel&nbsp; 178x475</h2>
  <section class="art wizard-panel" aria-label="Wizard left panel">
    <p class="wordmark" style="left:36px;top:76px;font-size:21px;">TALVERO</p>
    <p class="wordmark" style="left:36px;top:100px;font-size:21px;">NETWISE</p>
    <p class="tagline" style="left:37px;top:125px;font-size:12px;">Cloud Backup &amp; Recovery</p>
    <div class="disc" role="img" aria-label="Backup disc illustration" style="left:88px;top:238px;width:150px;height:150px;"></div>
    <div class="mark" style="left:-60px;top:290px;width:270px;height:270px;background:var(--navy);"></div>
  </section>

  <h2 class="label" style="left:789px;top:836px;">Left panel&nbsp; 146x314</h2>
  <section class="art left-panel" aria-label="Left panel">
    <div class="mark" style="left:62px;top:42px;width:140px;height:140px;background:rgba(255,255,255,.92);"></div>
    <div class="disc" role="img" aria-label="Backup disc illustration" style="left:10px;top:280px;width:98px;height:98px;"></div>
    <div class="disc" role="img" aria-label="Backup disc illustration" style="left:95px;top:325px;width:180px;height:180px;opacity:.8;"></div>
  </section>

</main>
</body>
</html>
```